truck graphics

Would like graphic design for work truck advertising. The truck uploaded without graphics is the truck. The other with graphics is a concept idea.

Company name Fernvale Grounds
731 482 5917
Use The name with the lines on top and bottom without the graphic

I like the green stripe of the truck but ours can say ‘Deeply Rooted In The Community’

On the bed of truck similar to picture
Lawn Care - Maintenance - Land Clearing - Bush Hogging

```html
<!DOCTYPE html>
<html lang="en">
<head>
<meta charset="utf-8">
<title>Fernvale Grounds – Truck Graphics</title>
<link href="https://fonts.googleapis.com/css2?family=Poppins:wght@600;700&family=Roboto+Condensed:wght@700&display=swap" rel="stylesheet">
<style>
  :root {
    --brand-green: #137a2e;
    --tree-green: #1a6e2c;
    --vinyl-white: #ffffff;
    --backdrop: #f3f4f1;
  }
  * { margin: 0; padding: 0; box-sizing: border-box; }
  html, body { width: 1200px; height: 1200px; overflow: hidden; background: var(--backdrop); }
  .canvas { position: relative; width: 1200px; height: 1200px; }
  .side { position: absolute; left: 0; width: 1200px; height: 600px; }
  .side--driver { top: 0; }
  .side--passenger { top: 600px; border-top: 1px solid #dfe2dc; }

  .stripe { position: absolute; left: 0; top: 0; width: 1200px; height: 600px; }
  .stripe polygon { fill: var(--brand-green); }

  .tagline {
    position: absolute; height: 30px; line-height: 30px;
    font-family: "Poppins", sans-serif; font-weight: 600; font-size: 17px;
    letter-spacing: 0.6px; color: var(--vinyl-white); white-space: nowrap;
  }

  .wordmark { position: absolute; width: 180px; color: var(--brand-green); text-align: center; font-family: "Poppins", sans-serif; }
  .wordmark__rule { height: 2px; background: var(--brand-green); }
  .wordmark__name { font-weight: 700; font-size: 35px; line-height: 40px; letter-spacing: 0; margin-top: 2px; white-space: nowrap; }
  .wordmark__sub { display: flex; align-items: center; gap: 6px; font-weight: 600; font-size: 13px; line-height: 16px; letter-spacing: 0.8px; margin-top: 2px; }
  .wordmark__sub::before, .wordmark__sub::after { content: ""; flex: 1; height: 2px; background: var(--brand-green); }

  .phone {
    position: absolute; font-family: "Roboto Condensed", sans-serif; font-weight: 700;
    font-size: 24px; line-height: 30px; color: var(--brand-green); white-space: nowrap; letter-spacing: -0.5px;
  }

  .services {
    position: absolute; font-family: "Poppins", sans-serif; font-weight: 600;
    font-size: 17px; line-height: 23px; color: var(--brand-green); white-space: nowrap; letter-spacing: 0.2px;
  }
  .services__line { display: block; }

  .tree-art {
    position: absolute; background: var(--tree-green);
    border: 3px solid var(--vinyl-white);
    border-radius: 48% 48% 22% 22% / 55% 55% 18% 18%;
  }
</style>
</head>
<body>
<main class="canvas">

  <section class="side side--driver">
    <svg class="stripe" viewBox="0 0 1200 600" aria-hidden="true">
      <polygon points="240,388 897,388 897,417 205,417"/>
    </svg>
    <div class="tagline" style="left:256px; top:389px;">DEEPLY ROOTED IN THE COMMUNITY</div>

    <div class="wordmark" style="left:264px; top:318px;">
      <div class="wordmark__rule"></div>
      <div class="wordmark__name">FERNVALE</div>
      <div class="wordmark__sub">GROUNDS</div>
    </div>

    <div class="phone" style="left:490px; top:286px;">731 482 5917</div>

    <div class="tree-art" role="img" aria-label="Green silhouette illustration of a large oak tree" style="left:620px; top:273px; width:172px; height:146px;"></div>

    <div class="services" style="left:790px; top:276px;">
      <span class="services__line" style="padding-left:18px;">• LAWN CARE &nbsp;• MAINTENANCE</span>
      <span class="services__line">• LAND CLEARING &nbsp;• BUSH HOGGING</span>
    </div>
  </section>

  <section class="side side--passenger">
    <svg class="stripe" viewBox="0 0 1200 600" aria-hidden="true">
      <polygon points="304,388 957,388 994,419 304,419"/>
    </svg>
    <div class="tagline" style="left:586px; top:389px;">DEEPLY ROOTED IN THE COMMUNITY</div>

    <div class="services" style="left:93px; top:275px;">
      <span class="services__line" style="padding-left:18px;">• LAWN CARE &nbsp;• MAINTENANCE</span>
      <span class="services__line">• LAND CLEARING &nbsp;• BUSH HOGGING</span>
    </div>

    <div class="tree-art" role="img" aria-label="Green silhouette illustration of a large oak tree" style="left:410px; top:273px; width:171px; height:146px;"></div>

    <div class="phone" style="left:586px; top:287px;">731 482 5917</div>

    <div class="wordmark" style="left:756px; top:318px;">
      <div class="wordmark__rule"></div>
      <div class="wordmark__name">FERNVALE</div>
      <div class="wordmark__sub">GROUNDS</div>
    </div>
  </section>

</main>
</body>
</html>
```